Tollbrook needs a modernized design

We would like a modern update (that can be responsive) to our existing website. Attached are the two existing pages we would like new concepts of - our home page and a page about one of our locations.

Tollbrook is provides executive offices and virtual office services. Startups, law firms, and financial services are our primary clients. We would like a professional, clean design, leaning towards minimalist. We intend to greatly reduce/eliminate the long paragraphs of text.

Industry/Entity Type

Business Service

Number of Pages Required

2 page

Requirements
Must have
• A design that can be responsive
Nice to have
• Large image(s) on home page that rotate.

```html
<!DOCTYPE html>
<html lang="en">
<head>
<meta charset="utf-8">
<title>Tollbrook Business Centers</title>
<link rel="stylesheet" href="https://fonts.googleapis.com/css2?family=Roboto+Condensed:wght@400;700&family=Open+Sans:wght@400;700&display=swap">
<style>
:root{
  --navy:#0b0a5e;
  --navy-band:#2c2a8a;
  --navy-band-deep:#1f1d78;
  --hero-a:#c9ccd3;
  --hero-b:#e9eaee;
  --ink:#555;
  --field-line:#c8c8c8;
  --soft-bg:#f2f2f2;
  --white:#fff;
}
*{box-sizing:border-box;margin:0;padding:0}
html,body{width:1200px;height:2305px;overflow:hidden;background:var(--white)}
body{position:relative;font-family:"Open Sans",Arial,sans-serif;color:var(--ink)}
.abs{position:absolute}
.cond{font-family:"Roboto Condensed","Arial Narrow",sans-serif}

/* header */
.brand{left:77px;top:12px;height:103px;display:flex;align-items:center;gap:16px}
.brand-dot{width:100px;height:100px;border-radius:50%;background:var(--navy)}
.brand-name{font-family:"Roboto Condensed",sans-serif;font-weight:700;font-size:48px;color:var(--navy);letter-spacing:1px}
.nav{left:461px;top:38px;display:flex;align-items:center;font-family:"Roboto Condensed",sans-serif;font-size:16px;color:#444;text-transform:uppercase}
.nav a{text-decoration:none;color:inherit;height:47px;line-height:47px}
.nav .active{background:var(--navy);color:var(--white);border-radius:24px;width:88px;text-align:center;margin-right:14px}
.nav a+a{margin-left:0}
.nav .item{margin-right:36px}

/* hero */
.hero{left:0;top:128px;width:1200px;height:574px;background:linear-gradient(110deg,var(--hero-a),var(--hero-b) 55%,#d7dae2)}
.hero-caption{left:77px;top:326px;width:425px;height:189px;background:rgba(40,38,140,.85);color:var(--white);font-family:"Roboto Condensed",sans-serif;font-size:31px;line-height:42px;padding:24px 24px}

/* welcome */
.welcome-title{left:0;width:1200px;top:762px;text-align:center;font-family:"Roboto Condensed",sans-serif;font-size:41px;color:var(--navy)}
.welcome-text{left:0;width:1200px;top:820px;text-align:center;font-size:15.5px;line-height:24px;color:#666}
.pill{background:var(--navy);color:var(--white);font-family:"Roboto Condensed",sans-serif;border-radius:24px;text-align:center;text-transform:uppercase}
.read-more{left:516px;top:897px;width:168px;height:45px;line-height:45px;font-size:22px}

/* services */
.services{left:0;top:1011px;width:1200px;height:303px;background:linear-gradient(180deg,var(--navy-band),var(--navy-band-deep))}
.services-foot{left:0;top:1283px;width:1200px;height:31px;background:#3b39a0}
.service{width:216px;text-align:center;color:var(--white);font-family:"Roboto Condensed",sans-serif;font-size:21px;line-height:31px;text-transform:uppercase;top:1067px}
.service-icon{width:104px;height:104px;border-radius:50%;background:var(--white);margin:0 auto 14px;display:flex;align-items:center;justify-content:center}

/* quote */
.quote-title{left:0;width:1200px;top:1362px;text-align:center;font-family:"Roboto Condensed",sans-serif;font-size:41px;color:var(--navy)}
.quote-sub{left:0;width:1200px;top:1415px;text-align:center;font-size:19px;color:var(--navy)}
.field{height:46px;border:1px solid var(--field-line);font-size:15px;color:#666;padding:0 10px;line-height:44px;background:var(--white)}
.field .caret{position:absolute;right:18px;top:19px}
.submit{left:538px;top:1747px;width:144px;height:45px;line-height:45px;font-size:22px}

/* promo */
.promo{left:0;top:1839px;width:1200px;height:215px;background:var(--soft-bg)}
.badge{left:79px;top:1875px;width:138px;height:138px;border-radius:50%;background:#8f98ac;border:8px solid #2d3f7a}
.promo-rule{left:250px;top:1888px;width:1px;height:122px;background:#cfcfcf}
.promo-title{left:281px;top:1898px;font-family:"Roboto Condensed",sans-serif;font-size:35px;color:var(--navy)}
.promo-text{left:281px;top:1952px;width:840px;font-size:15.5px;line-height:25px;color:#666}

/* footer */
.footer{left:0;top:2054px;width:1200px;height:251px;background:var(--navy);color:var(--white)}
.foot-links{list-style:none;font-size:15.5px;line-height:29px}
.foot-rule{width:1px;height:142px;top:2083px;background:#4a49a0}
.city{font-family:"Roboto Condensed",sans-serif;font-weight:700;font-size:21px}
.phone{font-family:"Roboto Condensed",sans-serif;font-size:22px;display:flex;align-items:center;gap:12px}
.follow{left:708px;top:2084px;font-family:"Roboto Condensed",sans-serif;font-size:31px}
.social{width:46px;height:46px;border-radius:50%;border:2px solid var(--white);top:2139px}
.social.filled{background:var(--white)}
.foot-line{left:77px;top:2252px;width:1046px;height:1px;background:#4a49a0}
.copyright{left:0;width:1200px;top:2265px;text-align:center;font-size:15px}
.copyright b{font-weight:700}
</style>
</head>
<body>

<header>
  <div class="abs brand"><span class="brand-dot"></span><span class="brand-name">TOLLBROOK</span></div>
  <nav class="abs nav">
    <a class="active" href="#">Home</a>
    <a class="item" href="#">Properties</a>
    <a class="item" href="#">Virtual Tours &amp; Videos</a>
    <a class="item" href="#">Photos</a>
    <a href="#">Broker Referrals</a>
  </nav>
</header>

<section class="abs hero" role="img" aria-label="Photo of three smiling business professionals gathered around a laptop in a bright office"></section>
<div class="abs hero-caption">Cost Effective Virtual Office Solutions. Customized Corporate Image.</div>

<h1 class="abs welcome-title">WELCOME TO TOLLBROOK BUSINESS CENTERS</h1>
<p class="abs welcome-text">Come See Why Smarter Companies are Choosing Tollbrook Business Centers' Dallas, Ft. Worth and<br>Houston Executive Office Suites, Virtual Offices, Meeting Rooms and Video Conferencing.</p>
<div class="abs pill read-more">Read More</div>

<section class="abs services" role="img" aria-label="Blue tinted city skyline background"></section>
<div class="abs services-foot"></div>

<div class="abs service" style="left:59px">
  <div class="service-icon"><svg width="50" height="50" viewBox="0 0 50 50" fill="#0b0a5e"><circle cx="25" cy="10" r="6"/><path d="M16 26c0-6 4-9 9-9s9 3 9 9z"/><rect x="8" y="26" width="34" height="5"/><path d="M12 31h26l-3 15H15z"/></svg></div>
  Executive Office<br>Suites
</div>
<div class="abs service" style="left:275px">
  <div class="service-icon"><svg width="50" height="50" viewBox="0 0 50 50" fill="#0b0a5e"><circle cx="12" cy="9" r="4"/><circle cx="25" cy="7" r="4"/><circle cx="38" cy="9" r="4"/><rect x="8" y="15" width="8" height="12" rx="2"/><rect x="34" y="15" width="8" height="12" rx="2"/><rect x="17" y="20" width="16" height="4"/><rect x="23" y="24" width="4" height="20"/><rect x="8" y="28" width="3" height="16"/><rect x="39" y="28" width="3" height="16"/></svg></div>
  On-Demand<br>Meeting Rooms
</div>
<div class="abs service" style="left:490px">
  <div class="service-icon"><svg width="50" height="50" viewBox="0 0 50 50" fill="#0b0a5e"><rect x="18" y="4" width="26" height="16" fill="none" stroke="#0b0a5e" stroke-width="3"/><circle cx="12" cy="12" r="4"/><path d="M7 30v-8c0-3 2-4 5-4h8l-2 4h-3v8z"/><circle cx="14" cy="33" r="3"/><circle cx="25" cy="33" r="3"/><circle cx="36" cy="33" r="3"/><rect x="9" y="37" width="10" height="7"/><rect x="20" y="37" width="10" height="7"/><rect x="31" y="37" width="10" height="7"/></svg></div>
  On-Demand<br>Training Rooms
</div>
<div class="abs service" style="left:706px">
  <div class="service-icon"><svg width="50" height="50" viewBox="0 0 50 50" fill="#0b0a5e"><circle cx="14" cy="9" r="4"/><path d="M10 15h7l3 10h8v4H17l-2 14h-4l1-14-3-2z"/><rect x="26" y="6" width="18" height="14" fill="none" stroke="#0b0a5e" stroke-width="3"/><rect x="22" y="24" width="24" height="3"/><rect x="40" y="27" width="3" height="17"/></svg></div>
  Virtual Office<br>Solutions
</div>
<div class="abs service" style="left:917px">
  <div class="service-icon"><svg width="50" height="50" viewBox="0 0 50 50" fill="#0b0a5e"><rect x="12" y="4" width="26" height="16" fill="none" stroke="#0b0a5e" stroke-width="3"/><circle cx="25" cy="11" r="3"/><circle cx="10" cy="27" r="3"/><circle cx="40" cy="27" r="3"/><rect x="6" y="31" width="8" height="8" rx="2"/><rect x="36" y="31" width="8" height="8" rx="2"/><rect x="15" y="30" width="20" height="3"/><rect x="23" y="33" width="4" height="11"/><rect x="6" y="40" width="3" height="5"/><rect x="41" y="40" width="3" height="5"/></svg></div>
  Video Conference<br>Solutions
</div>

<h2 class="abs quote-title">GET FREE QUOTE</h2>
<p class="abs quote-sub">WE WOULD LOVE TO TALK WITH YOU</p>

<div class="abs field" style="left:246px;top:1475px;width:353px">Enter First Name</div>
<div class="abs field" style="left:621px;top:1475px;width:353px">Enter Last Name</div>
<div class="abs field" style="left:246px;top:1543px;width:353px">Enter Company Name</div>
<div class="abs field" style="left:621px;top:1543px;width:353px">Enter Contact No.</div>
<div class="abs field" style="left:246px;top:1610px;width:728px">Enter Email Id</div>
<div class="abs field" style="left:246px;top:1678px;width:353px">Enter Property Interested In<svg class="caret" width="18" height="10" viewBox="0 0 18 10"><path d="M0 0h18L9 10z" fill="#0b0a5e"/></svg></div>
<div class="abs field" style="left:621px;top:1678px;width:353px">Enter Product Interested In<svg class="caret" width="18" height="10" viewBox="0 0 18 10"><path d="M0 0h18L9 10z" fill="#0b0a5e"/></svg></div>
<div class="abs pill submit">Submit</div>

<section class="abs promo"></section>
<div class="abs badge"></div>
<div class="abs promo-rule"></div>
<h2 class="abs promo-title">SPRING INTO THE PERFECT OFFICE WITH TOLLBROOK</h2>
<p class="abs promo-text">Lorem Ipsum is simply dummy text of the printing and typesetting industry. Lorem Ipsum has been the industry's standard dummy text ever since the 1500.</p>

<footer class="abs footer"></footer>
<ul class="abs foot-links" style="left:80px;top:2079px;color:#fff"><li>About Us</li><li>Contact Us</li><li>Forms</li><li>Testimonials</li><li>FAQs</li></ul>
<ul class="abs foot-links" style="left:267px;top:2079px;color:#fff"><li>Careers</li><li>Furniture</li><li>Specials</li><li>Site Map</li><li>Privacy</li></ul>
<div class="abs foot-rule" style="left:409px"></div>
<div class="abs city" style="left:450px;top:2080px;color:#fff">Dallas</div>
<div class="abs phone" style="left:450px;top:2111px;color:#fff"><svg width="20" height="20" viewBox="0 0 24 24" fill="#fff"><path d="M6.6 10.8a15 15 0 0 0 6.6 6.6l2.2-2.2a1 1 0 0 1 1-.25 11.4 11.4 0 0 0 3.6.57 1 1 0 0 1 1 1V20a1 1 0 0 1-1 1A17 17 0 0 1 3 4a1 1 0 0 1 1-1h3.5a1 1 0 0 1 1 1c0 1.25.2 2.45.57 3.57a1 1 0 0 1-.25 1z"/></svg>214.555.0143</div>
<div class="abs city" style="left:450px;top:2163px;color:#fff">Houston</div>
<div class="abs phone" style="left:450px;top:2194px;color:#fff"><svg width="20" height="20" viewBox="0 0 24 24" fill="#fff"><path d="M6.6 10.8a15 15 0 0 0 6.6 6.6l2.2-2.2a1 1 0 0 1 1-.25 11.4 11.4 0 0 0 3.6.57 1 1 0 0 1 1 1V20a1 1 0 0 1-1 1A17 17 0 0 1 3 4a1 1 0 0 1 1-1h3.5a1 1 0 0 1 1 1c0 1.25.2 2.45.57 3.57a1 1 0 0 1-.25 1z"/></svg>713.555.0178</div>
<div class="abs foot-rule" style="left:671px"></div>
<div class="abs follow" style="color:#fff">Follow us</div>
<span class="abs social filled" style="left:708px"></span>
<span class="abs social" style="left:770px"></span>
<span class="abs social" style="left:833px"></span>
<span class="abs social" style="left:894px"></span>
<span class="abs social" style="left:957px"></span>
<div class="abs foot-line"></div>
<p class="abs copyright" style="color:#fff">© <b>Tollbrook Business Centers</b> - 2016. All Rights Reserved.</p>

</body>
</html>
```